CEO Business card - hotels and restaurant

Business card for the General Manager of 3 different businesses: 2 hotels and 1 restaurant:
Quinta Serrana Hotel
Casa Ormonde - Miravel Hotel
pão com toda alegria restaurant
Name and contact details:
Rui Fontelas Marques
CEO
E-mail: rui.marques@quintaserranahotel.com
Mobile: +351 917 443 261
Please find the attached logos. You may also google it for the 3 businesses

Industry/Entity Type

Hospitality

Contact Information for Business Card

Rui Fontelas Marques
CEO

Font styles to use
Script

Colors

Designer to choose colors to be used in the design.

Requirements
Must have
• Front - Name, position and contact details
• Back - Businesses logos and info of each one
• HOTEL QUINTA SERRANA
• Address: Rua Padre Anselmo - Nº 173 | 2440-627 BATALHA - PORTUGAL
• Phone: +351 244 581 392
• E-mail: geral@quintaserranahotel.pt
• HOTEL CASA ORMONDE - MIRAVEL
• Address: Avenida dos Cedros, s/n | 7350-218 ELVAS - PORTUGAL
• Phone: +351 268 472 519
• E-mail: geral@hotelcormonde-miravel.pt
• "pão com toda alegria" RESTAURANT
• Address: Estrada do Pinhal, 42 | 2440-356 BATALHA - PORTUGAL
• Phone: +351 244 615 284
• E-mail: info@pcta.pt
Nice to have
• Something elegant and stylish but professional and very wow effect

```html
<!DOCTYPE html>
<html lang="pt">
<head>
<meta charset="utf-8">
<title>Rui Fontelas Marques – Business Card</title>
<link href="https://fonts.googleapis.com/css2?family=Days+One&family=Pathway+Gothic+One&display=swap" rel="stylesheet">
<style>
  :root {
    --ink: #000000;
    --stone: #939598;
    --magenta: #ec008c;
    --paper: #ffffff;
    --backdrop: #d9d4cc;
    --shade: #c9c9c9;
  }
  * { margin: 0; padding: 0; box-sizing: border-box; }
  html, body { width: 1200px; height: 1200px; overflow: hidden; }
  body { background: var(--backdrop); position: relative; font-family: "Pathway Gothic One", sans-serif; }

  .card {
    position: absolute; left: 211px; width: 778px; height: 466px;
    background: var(--paper); overflow: hidden;
    box-shadow: 0 6px 18px rgba(0,0,0,0.25);
  }
  .card--front { top: 90px; }
  .card--back { top: 644px; }

  /* front */
  .brand-marks { position: absolute; inset: 0; }
  .brand-mark { position: absolute; border-radius: 50%; }
  .brand-mark--restaurant { left: 539px; top: 44px; width: 104px; height: 104px; background: var(--ink); transform: translateX(-211px); }
  .brand-mark--hotel-cast { left: 404px; top: 168px; width: 114px; height: 114px; background: var(--stone); }
  .brand-mark--hotel-quinta { left: 262px; top: 168px; width: 114px; height: 114px; background: var(--magenta); }

  .brand-names { position: absolute; top: 304px; left: 0; right: 0; text-align: center; font-family: "Days One", sans-serif; }
  .brand-names p { font-size: 20px; line-height: 33px; letter-spacing: 0.5px; }
  .brand-names .restaurant { color: var(--ink); }
  .brand-names .hotel-cast { color: var(--stone); }
  .brand-names .hotel-quinta { color: var(--magenta); }

  .fold-shade { position: absolute; left: 0; right: 0; height: 16px; background: linear-gradient(to bottom, rgba(255,255,255,0), var(--shade)); }
  .card--front .fold-shade { top: 411px; }
  .color-band { position: absolute; left: 0; right: 0; bottom: 0; height: 39px; display: flex; }
  .color-band span { flex: 1; }
  .band-ink { background: var(--ink); }
  .band-stone { background: var(--stone); }
  .band-magenta { background: var(--magenta); }

  /* back */
  .person { position: absolute; left: 37px; top: 38px; color: var(--ink); }
  .person-name { font-family: "Days One", sans-serif; font-size: 26px; line-height: 32px; }
  .person-role { font-size: 17px; letter-spacing: 8px; line-height: 22px; margin-bottom: 4px; }
  .contact-line { display: flex; align-items: center; gap: 6px; font-size: 24px; line-height: 31px; }
  .icon { width: 26px; height: 26px; flex: none; }
  .card--back .fold-shade { top: 182px; }

  .venues { position: absolute; left: 0; right: 0; top: 198px; height: 268px; display: flex; }
  .venue { flex: 1; color: var(--paper); text-align: center; display: flex; flex-direction: column; align-items: center; padding-top: 20px; }
  .venue--restaurant { background: var(--ink); }
  .venue--hotel-cast { background: var(--stone); }
  .venue--hotel-quinta { background: var(--magenta); }
  .venue-mark { width: 44px; height: 44px; background: var(--paper); border-radius: 50%; }
  .venue-name { font-family: "Days One", sans-serif; font-size: 19px; line-height: 21px; height: 48px; display: flex; align-items: flex-end; justify-content: center; padding: 0 10px; }
  .venue-type { font-family: "Days One", sans-serif; font-size: 12px; letter-spacing: 9px; margin: 12px 0 4px; padding-left: 9px; }
  .venue-address { font-size: 20px; line-height: 24px; }
  .venue .contact-line { font-size: 20px; line-height: 28px; justify-content: center; margin-top: 2px; }
  .venue .icon { width: 24px; height: 24px; }
</style>
</head>
<body>
<svg width="0" height="0" style="position:absolute" aria-hidden="true">
  <defs>
    <symbol id="icon-mail" viewBox="0 0 26 26">
      <circle cx="13" cy="13" r="12" fill="currentColor"/>
      <rect x="6.5" y="8.5" width="13" height="9" rx="1" fill="none" stroke="#fff" stroke-width="1.6"/>
      <path d="M6.8 9 L13 14 L19.2 9" fill="none" stroke="#fff" stroke-width="1.6"/>
    </symbol>
    <symbol id="icon-phone" viewBox="0 0 26 26">
      <circle cx="13" cy="13" r="12" fill="currentColor"/>
      <path d="M10 6.5 C8 7.5 7.2 10 8 13 C9 16.5 11.5 19 14.5 19.8 L16.5 17.5 L14.5 15.5 L12.8 16.2 C11.6 15 10.8 13.5 10.6 11.8 L12.2 10.8 L11.5 7.2 Z" fill="#fff"/>
    </symbol>
  </defs>
</svg>

<section class="card card--front" aria-label="Card front">
  <div class="brand-marks">
    <span class="brand-mark brand-mark--restaurant" style="left:328px"></span>
    <span class="brand-mark brand-mark--hotel-quinta"></span>
    <span class="brand-mark brand-mark--hotel-cast"></span>
  </div>
  <div class="brand-names">
    <p class="restaurant">PÃO COM TODA ALEGRIA</p>
    <p class="hotel-cast">CASA ORMONDE - MIRAVEL</p>
    <p class="hotel-quinta">QUINTA SERRANA</p>
  </div>
  <div class="fold-shade"></div>
  <div class="color-band"><span class="band-ink"></span><span class="band-stone"></span><span class="band-magenta"></span></div>
</section>

<section class="card card--back" aria-label="Card back">
  <div class="person">
    <h1 class="person-name">Rui Fontelas Marques</h1>
    <p class="person-role">CEO</p>
    <p class="contact-line"><svg class="icon"><use href="#icon-mail"/></svg>rui.marques@quintaserranahotel.com</p>
    <p class="contact-line"><svg class="icon"><use href="#icon-phone"/></svg>+351 917 443 261</p>
  </div>
  <div class="fold-shade"></div>
  <div class="venues">
    <article class="venue venue--restaurant">
      <span class="venue-mark"></span>
      <h2 class="venue-name">Pão com Toda<br>Alegria</h2>
      <p class="venue-type">RESTAURANT</p>
      <p class="venue-address">Estrada do Pinhal, 42<br>2440-356 BATALHA - PORTUGAL</p>
      <p class="contact-line"><svg class="icon" style="color:#fff"><use href="#icon-phone" style="color:#fff"/></svg>+351 244 615 284</p>
      <p class="contact-line"><svg class="icon"><use href="#icon-mail" style="color:#fff"/></svg>info@pcta.pt</p>
    </article>
    <article class="venue venue--hotel-cast">
      <span class="venue-mark"></span>
      <h2 class="venue-name">Casa Ormonde - Miravel</h2>
      <p class="venue-type">HOTEL</p>
      <p class="venue-address">Avenida dos Cedros s/n<br>7350-218 ELVAS - PORTUGAL</p>
      <p class="contact-line"><svg class="icon"><use href="#icon-phone" style="color:#fff"/></svg>+351 268 472 519</p>
      <p class="contact-line"><svg class="icon"><use href="#icon-mail" style="color:#fff"/></svg>geral@hotelcormonde-miravel.pt</p>
    </article>
    <article class="venue venue--hotel-quinta">
      <span class="venue-mark"></span>
      <h2 class="venue-name">Quinta Serrana</h2>
      <p class="venue-type">HOTEL</p>
      <p class="venue-address">Rua Padre Anselmo - Nº 173<br>2440-627 BATALHA - PORTUGAL</p>
      <p class="contact-line"><svg class="icon"><use href="#icon-phone" style="color:#fff"/></svg>+351 244 581 392</p>
      <p class="contact-line"><svg class="icon"><use href="#icon-mail" style="color:#fff"/></svg>geral@quintaserranahotel.pt</p>
    </article>
  </div>
</section>
</body>
</html>
```